Brook & Thistle Labels*

Hello :) I am needing labels for my herbal tea/petal product. I am a small producer for the local restaurants (edible flowers/micro herbs & dried product). I am hoping to sell the dried product online. It will be sold in batches as it is ready so quite small/boutique and the label needs to be somewhat generic for the range of produce I make.
Feels: no/minimal plastic, product is in a reusable mason jar, we use organic/regenerative principles from soil health to end product. Treading gently on the land. High quality i.e only fresh hand picked leaf tips for the tea.

```html
<!DOCTYPE html>
<html lang="en">
<head>
<meta charset="utf-8">
<title>Brook &amp; Thistle — Label</title>
<link rel="stylesheet" href="https://fonts.googleapis.com/css2?family=Parisienne&family=Pathway+Gothic+One&family=Nunito:wght@700&display=swap">
<style>
  :root {
    --page-bg: #e4e4e6;
    --leaf-deep: #04210c;
    --leaf-mid: #0c4a1c;
    --leaf-bright: #16652a;
    --ink-light: #f1f1f1;
    --ink-green: #1c4a27;
  }
  * { margin: 0; padding: 0; box-sizing: border-box; }
  html, body {
    width: 1200px;
    height: 919px;
    overflow: hidden;
    background: var(--page-bg);
  }
  .canvas {
    position: relative;
    width: 1200px;
    height: 919px;
  }
  .label {
    position: absolute;
    left: 101px;
    top: 85px;
    width: 997px;
    height: 749px;
    overflow: hidden;
  }
  .label__foliage {
    position: absolute;
    inset: 0;
    background:
      radial-gradient(ellipse at 25% 30%, var(--leaf-bright) 0%, transparent 45%),
      radial-gradient(ellipse at 78% 65%, var(--leaf-bright) 0%, transparent 40%),
      radial-gradient(ellipse at 50% 90%, var(--leaf-mid) 0%, transparent 50%),
      linear-gradient(160deg, var(--leaf-mid) 0%, var(--leaf-deep) 55%, var(--leaf-mid) 100%);
  }
  .label__frame {
    position: absolute;
    left: 0;
    top: 0;
  }
  .brand-seal {
    position: absolute;
    left: 454px;
    top: 63px;
    width: 104px;
    height: 104px;
    border-radius: 50%;
    background: var(--ink-light);
    display: flex;
    align-items: center;
    justify-content: center;
  }
  .brand-seal__name {
    font-family: "Nunito", sans-serif;
    font-weight: 700;
    font-size: 15px;
    color: var(--ink-green);
    white-space: nowrap;
  }
  .product-title {
    font-family: "Parisienne", cursive;
    color: var(--ink-light);
    font-weight: 400;
  }
  .product-title span {
    position: absolute;
    line-height: 1;
    white-space: nowrap;
  }
  .product-title__first {
    left: 368px;
    top: 236px;
    font-size: 54px;
  }
  .product-title__amp {
    left: 446px;
    top: 306px;
    font-size: 36px;
  }
  .product-title__second {
    left: 474px;
    top: 290px;
    font-size: 54px;
  }
  .title-rule {
    position: absolute;
    left: 465px;
    top: 454px;
    width: 84px;
    height: 3px;
    background: var(--ink-light);
  }
  .tagline {
    position: absolute;
    left: 407px;
    top: 488px;
    width: 200px;
    text-align: center;
    font-family: "Pathway Gothic One", sans-serif;
    font-size: 13px;
    line-height: 20px;
    letter-spacing: 0.5px;
    color: var(--ink-light);
    text-transform: uppercase;
  }
  .produce-badge {
    position: absolute;
    left: 454px;
    top: 566px;
    width: 104px;
    height: 104px;
    border-radius: 50%;
    background: var(--ink-light);
  }
</style>
</head>
<body>
  <main class="canvas">
    <section class="label">
      <div class="label__foliage" role="img" aria-label="Dense pattern of deep green tea leaves covering the whole label"></div>

      <svg class="label__frame" width="997" height="749" viewBox="0 0 997 749" aria-hidden="true">
        <g fill="none" stroke="#f1f1f1" stroke-width="3">
          <path d="M420 70 H339 V658 H420"/>
          <path d="M581 70 H658 V658 H581"/>
        </g>
      </svg>

      <div class="brand-seal">
        <span class="brand-seal__name">Verdant Row</span>
      </div>

      <h1 class="product-title">
        <span class="product-title__first">Brook</span>
        <span class="product-title__amp">&amp;</span>
        <span class="product-title__second">Thistle</span>
      </h1>

      <div class="title-rule"></div>

      <p class="tagline">
        Grown, harvested and dried<br>
        chemical free on our farm<br>
        in Tallow Creek
      </p>

      <div class="produce-badge" role="img" aria-label="Regional produce badge"></div>
    </section>
  </main>
</body>
</html>
```